Website design for Cambridge based systematic hedge fund

We have run previous craftmosaic competitions to design our company logo, business cards and the styling of our presentation deck (see attached files).
As the final step we are looking to get a website designed that is thematically consistent with these existing elements of our branding.
You can find some of our competitors websites below:
https://www.quelmarsh.example/
https://www.fenloor.example/
https://www.pyvart.example/
https://www.dulvet.example/
https://www.orbelmfunds.example/
https://www.valtrigo.example/
https://www.meskilfunds.example/home
We would like to have a website that works well on both mobile devices and desktops. Either just as one page that can be scrolled down, with links at the top that skips to certain sections, or a few separate pages that can be navigated by a top menu.
It should look professional, we are not after lots of animations or unnecessary transitions, and in particular the website must be smooth to navigate. We would like to avoid having peoples of people, we are happy to make use of elements from the presentation (for example the style of the cover slide, or the section slides with the faded bridge in the background), or 'financial' style images.
We would like to have the following sections for now. For some of these some example text has been provided, final text may change but it will be of similar length. For the other sections we are happy to just have template text for now. At the moment we are mainly interested to see styles/layouts as words can be added easily afterwards:
1) We will need a disclaimer pop up the first time someone visits the site (see for example the meskilfunds example).
2) Top page - company name, then in larger text "Bringing AI and Statistical Inference to Financial Markets", and somewhere in smaller text "Harlow Vectors is a quantitative asset manager with the singular focus of delivering algorithmic strategies that work"
3) "About us" section: will describe us as a company, details our approach, company values, and explains the company logo.
Example text:
"We deliver consistent alpha across liquid markets through the application of proprietary IP in Bayesian inference, machine learning and artificial intelligence. We are a multi-disciplinary team founded by experienced finance professionals from premier institutions, leading academics from the Thornbury Stellar Unit at Ashmere College and world-class software engineers.
Our logo portrays a sillhoute of the lattice walkway at Ashmere College. Our unique scientific approach allows us to bridge cutting-edge mathematical research and computing expertise with financial knowledge to bring algorithmns that work to liquid markets"
4) Hiring section, detailing our culture, what we are looking for.
Example text:
"We are always looking for exceptional talent to join our entrepreneurial team. We are looking for individuals who are creative thinkers, can demonstrate analytical rigour and are passionate about the intersection of science, finance and technology.
We prioritise having a company culture that promotes sharing ideas in a safe, collaborative research environment. We make sure that every member of the team has the oppertunity to explore their own ideas through weekly 'innovation time', and ensure that everyone gets the support they need to continue to grow as individuals within the company."
5) A section for news/press releases
6) Contact us area at the bottom with office location and email. We will need to list 3 addresses for our Cambridge, London and Singapore offices, along with a couple of contact emails or phone numbers
7) A client login button at the top that will take them to a different website (unrelated to this one).

```html
<!DOCTYPE html>
<html lang="en">
<head>
<meta charset="utf-8">
<title>Harlow Vectors</title>
<link rel="stylesheet" href="https://fonts.googleapis.com/css2?family=Montserrat:wght@400;500;600;700&display=swap">
<style>
:root{
  --backdrop:#b9d5f6;
  --navy:#0b2555;
  --ocean:#08437a;
  --footer:#0a3463;
  --orange:#f57c0c;
  --mist:#f2f6fb;
  --ink:#1d2633;
  --muted:#7b8494;
  --line:#e3e8ef;
  --accent:#3d8fd8;
  --white:#ffffff;
}
*{box-sizing:border-box;margin:0;padding:0}
html,body{width:1200px;height:3623px;overflow:hidden}
body{background:var(--backdrop);font-family:'Montserrat',sans-serif;color:var(--ink)}
.page{position:absolute;left:297px;top:0;width:605px;height:3623px;background:var(--white);overflow:hidden}
.btn{position:absolute;background:var(--orange);color:var(--white);font-size:7px;font-weight:500;border-radius:3px;display:flex;align-items:center;justify-content:center}
.rule{position:absolute;height:1px;width:34px;background:var(--accent)}
.tiny{font-size:6.5px;line-height:10.5px;color:var(--muted)}
.photo{position:absolute}
/* nav */
.topnav{position:absolute;top:0;left:0;width:605px;height:31px;background:var(--white)}
.brand{position:absolute;left:45px;top:10px;font-size:8px;font-weight:700;color:var(--navy)}
.menu{position:absolute;left:288px;top:12px;display:flex;gap:17px;font-size:6px;font-weight:600;color:var(--navy)}
.menu .on{color:var(--accent);border-bottom:1.5px solid var(--accent);padding-bottom:7px}
/* hero */
.hero{position:absolute;top:31px;left:0;width:605px;height:309px;background:radial-gradient(ellipse at 75% 40%,#17407e 0%,var(--navy) 60%)}
.hero .kicker{position:absolute;left:45px;top:36px;font-size:7px;font-weight:600;letter-spacing:1px;color:#9fc3ea;text-transform:uppercase}
.hero h1{position:absolute;left:45px;top:52px;width:330px;font-size:25px;line-height:31px;font-weight:700;color:var(--white)}
.hero p{position:absolute;left:45px;top:155px;width:215px;font-size:6.5px;line-height:10.5px;color:#d6e2f3}
/* intro */
.intro{position:absolute;top:340px;left:0;width:605px;height:653px;background:var(--mist)}
.card{position:absolute;left:63px;top:85px;width:239px;height:263px;background:var(--white)}
.card h2{position:absolute;left:19px;top:19px;font-size:14px;line-height:20px;font-weight:700}
.card .tiny{position:absolute;left:19px;top:72px;width:185px;font-size:6px;line-height:10px}
.partners-title{position:absolute;left:63px;top:453px;font-size:17px;font-weight:600}
.partner{position:absolute;top:518px;width:115px;height:72px;background:var(--white);border:1px solid var(--line);display:flex;align-items:center;justify-content:center}
.partner span{display:block;width:60px;height:16px;background:#c9ced6;border-radius:3px}
/* approach */
.approach{position:absolute;top:993px;left:0;width:605px;height:307px;background:var(--ocean);color:var(--white);text-align:center}
.approach h2{position:absolute;top:24px;width:100%;font-size:17px;font-weight:600}
.approach .lead{position:absolute;top:51px;left:190px;width:225px;font-size:5.5px;line-height:10.5px;color:#c7d8ea}
.step{position:absolute;top:145px;width:100px;text-align:left}
.num{width:22px;height:22px;border-radius:50%;background:var(--accent);font-size:11px;display:flex;align-items:center;justify-content:center}
.step h3{margin-top:8px;font-size:6.5px;line-height:10px;font-weight:600}
.step p{margin-top:6px;font-size:5.5px;line-height:9.5px;color:#c7d8ea}
/* values */
.values h2{position:absolute;left:63px;top:1364px;font-size:18px;line-height:25px;font-weight:600}
.values .intro-text{position:absolute;left:63px;top:1420px;width:200px}
.value{position:absolute;width:92px;height:92px;padding:14px 12px}
.value.raised{background:var(--white);box-shadow:0 2px 10px rgba(20,40,80,.1)}
.value svg{display:block}
.value h3{font-size:6px;font-weight:600;margin-top:6px}
.value p{font-size:5px;line-height:8px;color:var(--muted);margin-top:8px}
/* feature */
.feature h2{position:absolute;left:63px;top:1733px;font-size:25px;line-height:31px;font-weight:600}
.feature .tiny{position:absolute;left:63px;top:1805px;width:480px;font-size:6px;line-height:10.5px}
.col h2{position:absolute;top:2190px;font-size:15px;line-height:20px;font-weight:600}
.col .tiny{position:absolute;top:2240px;width:185px}
/* hiring */
.hiring{position:absolute;top:2612px;left:0;width:605px;height:511px;background:var(--ocean);color:var(--white)}
.hiring h2{position:absolute;top:34px;width:100%;text-align:center;font-size:17px;font-weight:600}
.tab{position:absolute;top:88px;height:20px;border:1px solid #c7d8ea;border-radius:10px;font-size:6.5px;display:flex;align-items:center;justify-content:center}
.tab.on{background:var(--white);color:var(--ocean)}
.count{position:absolute;left:45px;top:151px;font-size:8px}
.job{position:absolute;width:253px;height:56px;background:var(--mist);border:1px solid #d7dfe9;color:var(--ink);padding:13px 12px}
.job h3{font-size:8px;font-weight:600}
.job p{font-size:7px;color:var(--muted);margin-top:8px}
.more{position:absolute;top:389px;width:100%;text-align:center;font-size:8px;font-weight:600;text-decoration:underline}
.cta{position:absolute;left:45px;top:436px;font-size:8.5px;line-height:16px;font-weight:600}
/* contact */
.contact h2{position:absolute;top:3148px;width:100%;text-align:center;font-size:17px;font-weight:600}
.info{position:absolute;left:318px;top:3236px;width:225px;height:143px;background:var(--white);box-shadow:0 2px 12px rgba(20,40,80,.1)}
.info .row{position:absolute;left:46px;display:flex;align-items:center;gap:8px;font-size:6px;color:var(--muted)}
/* footer */
.foot{position:absolute;top:3464px;left:0;width:605px;height:159px;background:var(--footer);color:var(--white)}
.foot .mark{position:absolute;left:0;top:26px;width:605px;text-align:center;font-size:9px;font-weight:700}
.foot nav{position:absolute;left:0;top:60px;width:605px;display:flex;justify-content:center;gap:17px;font-size:6px;font-weight:600}
.foot .social{position:absolute;left:0;top:86px;width:605px;display:flex;justify-content:center;gap:6px}
.foot .social span{width:8px;height:8px;border:1px solid var(--white);border-radius:50%}
.foot .divider{position:absolute;top:116px;left:0;width:605px;height:1px;background:#2a5283}
.foot .legal{position:absolute;left:0;top:138px;width:605px;text-align:center;font-size:5px;color:#b9c9de}
</style>
</head>
<body>
<div class="page">

  <header class="topnav">
    <div class="brand">Harlow Vectors</div>
    <nav class="menu"><span class="on">HOME</span><span>ABOUT</span><span>APPROACH</span><span>VALUE</span><span>CULTURE</span></nav>
    <div class="btn" style="left:503px;top:6px;width:57px;height:20px">Client log in</div>
  </header>

  <section class="hero">
    <div class="photo" role="img" aria-label="Glowing blue network of connected data points" style="left:290px;top:0;width:315px;height:309px;background:radial-gradient(circle at 60% 45%,rgba(61,143,216,.45),rgba(11,37,85,0) 65%)"></div>
    <div class="kicker">Harlow Vectors</div>
    <h1>Bringing AI and Statistical Inference to Financial Markets</h1>
    <p>Harlow Vectors is a quantitative asset manager with the singular focus of delivering algorithmic strategies that work.</p>
    <div class="btn" style="left:45px;top:200px;width:67px;height:21px">Contact us</div>
  </section>

  <section class="intro">
    <div class="card">
      <h2>About Harlow<br>Vectors</h2>
      <div class="rule" style="left:19px;top:63px"></div>
      <p class="tiny">We deliver consistent alpha across liquid markets through the application of proprietary IP in Bayesian inference, machine learning and artificial intelligence. We are a multi-disciplinary team founded by experienced finance professionals from premier institutions, leading academics from the Thornbury Stellar Unit at Ashmere College and world-class software engineers.</p>
      <div class="btn" style="left:19px;top:201px;width:67px;height:21px">View more</div>
    </div>
    <div class="photo" role="img" aria-label="Financial charts and market data on a desk" style="left:305px;top:65px;width:238px;height:303px;background:linear-gradient(160deg,#d9dde3,#9aa3ad 60%,#e6e8ea)"></div>
    <h2 class="partners-title">Our Partners</h2>
    <div class="rule" style="left:63px;top:485px"></div>
    <div class="partner" style="left:63px"><span></span></div>
    <div class="partner" style="left:184px"><span></span></div>
    <div class="partner" style="left:305px"><span></span></div>
    <div class="partner" style="left:426px"><span></span></div>
  </section>

  <section class="approach">
    <h2>Approach</h2>
    <p class="lead">We bridge cutting-edge mathematical research and computing expertise with financial knowledge to bring algorithms that work to liquid markets.</p>
    <div class="rule" style="left:285px;top:91px;background:#7fb2e3"></div>
    <div class="step" style="left:63px"><div class="num">01</div><h3>Bayesian<br>inference</h3><p>Probabilistic models that quantify uncertainty in every market signal.</p></div>
    <div class="step" style="left:193px"><div class="num">02</div><h3>Machine<br>learning</h3><p>Proprietary methods that learn robust patterns across liquid markets.</p></div>
    <div class="step" style="left:322px"><div class="num">03</div><h3>Artificial<br>intelligence</h3><p>Systematic decisions built on research, not on human intuition alone.</p></div>
    <div class="step" style="left:451px"><div class="num">04</div><h3>World-class<br>engineering</h3><p>Reliable software that turns research into live trading strategies.</p></div>
  </section>

  <section class="values">
    <h2>Our Company<br>Values</h2>
    <p class="tiny intro-text">We prioritise a culture that promotes sharing ideas in a safe, collaborative research environment where every member of the team can grow.</p>
    <div class="value raised" style="left:51px;top:1475px">
      <svg width="12" height="10" viewBox="0 0 12 10"><circle cx="6" cy="3" r="2.2" fill="#3d8fd8"/><path d="M1 9 Q6 5 11 9" stroke="#3d8fd8" stroke-width="1.5" fill="none"/></svg>
      <h3>Creativity</h3><p>We value creative thinkers who explore new ideas with curiosity.</p></div>
    <div class="value" style="left:174px;top:1475px">
      <svg width="12" height="10" viewBox="0 0 12 10"><circle cx="6" cy="3" r="2.2" fill="#3d8fd8"/><path d="M1 9 Q6 5 11 9" stroke="#3d8fd8" stroke-width="1.5" fill="none"/></svg>
      <h3>Rigour</h3><p>Analytical rigour sits at the heart of every model we build.</p></div>
    <div class="value" style="left:51px;top:1575px">
      <svg width="12" height="10" viewBox="0 0 12 10"><circle cx="6" cy="3" r="2.2" fill="#3d8fd8"/><path d="M1 9 Q6 5 11 9" stroke="#3d8fd8" stroke-width="1.5" fill="none"/></svg>
      <h3>Collaboration</h3><p>Ideas are shared openly in a safe research environment.</p></div>
    <div class="value" style="left:174px;top:1575px">
      <svg width="12" height="10" viewBox="0 0 12 10"><circle cx="6" cy="3" r="2.2" fill="#3d8fd8"/><path d="M1 9 Q6 5 11 9" stroke="#3d8fd8" stroke-width="1.5" fill="none"/></svg>
      <h3>Growth</h3><p>Everyone gets the support they need to keep growing with us.</p></div>
    <div class="photo" role="img" aria-label="Modern office workspace with computer screens" style="left:314px;top:1365px;width:229px;height:287px;background:linear-gradient(170deg,#eceae6,#b9b4ac 55%,#8d877f)"></div>
  </section>

  <section class="feature">
    <h2>Bridging research<br>and markets</h2>
    <p class="tiny">Our logo portrays a silhouette of the lattice walkway at Ashmere College. Our unique scientific approach allows us to bridge cutting-edge mathematical research and computing expertise with financial knowledge to bring algorithms that work to liquid markets. We combine the discipline of academic science with the pace of modern finance, testing every idea with care before it reaches a live portfolio, and we keep refining our methods as markets and data evolve.</p>
    <div class="photo" role="img" aria-label="Faded lattice walkway over a river" style="left:45px;top:1871px;width:560px;height:252px;background:linear-gradient(100deg,#7a6a3a,#b79a5c 40%,#8a8275 70%,#4d5055)"></div>
  </section>

  <section class="col">
    <h2 style="left:45px">News and press<br>releases</h2>
    <p class="tiny" style="left:45px">The latest announcements from Harlow Vectors, from new research milestones to team updates and company press releases.</p>
    <div class="photo" role="img" aria-label="Stock market chart on a trading screen" style="left:45px;top:2297px;width:221px;height:252px;background:linear-gradient(170deg,#d8dadb,#9ea3a8 55%,#c6c8ca)"></div>
    <h2 style="left:339px">Weekly innovation<br>time</h2>
    <p class="tiny" style="left:339px">Every member of the team has the opportunity to explore their own ideas through weekly innovation time and research.</p>
    <div class="photo" role="img" aria-label="Financial data on a laptop screen" style="left:339px;top:2297px;width:221px;height:252px;background:linear-gradient(160deg,#f0f1f2,#c9ccd0 50%,#2f4466)"></div>
  </section>

  <section class="hiring">
    <h2>We are Hiring</h2>
    <div class="tab on" style="left:45px;width:60px">All Jobs</div>
    <div class="tab" style="left:112px;width:63px">Research</div>
    <div class="tab" style="left:182px;width:123px">Software Engineering</div>
    <p class="count">Showing all jobs (20)</p>
    <div class="job" style="left:45px;top:175px"><h3>Quantitative Researcher</h3><p>Harlow · Full time</p></div>
    <div class="job" style="left:308px;top:175px"><h3>Machine Learning Scientist</h3><p>London · Full time</p></div>
    <div class="job" style="left:45px;top:240px"><h3>Senior Software Engineer</h3><p>Harlow · Full time</p></div>
    <div class="job" style="left:308px;top:240px"><h3>Data Engineer</h3><p>Singapore · Full time</p></div>
    <div class="job" style="left:45px;top:306px"><h3>Quantitative Developer</h3><p>London · Full time</p></div>
    <div class="job" style="left:308px;top:306px"><h3>Research Intern</h3><p>Harlow · Summer</p></div>
    <p class="more">Show more</p>
    <p class="cta">Can't find your fit? Drop your CV and we'll reach<br>out when an opportunity comes up!</p>
    <div class="btn" style="left:464px;top:439px;width:96px;height:27px;font-size:8px">Drop your CV</div>
  </section>

  <section class="contact">
    <h2>Contact us</h2>
    <div class="photo" role="img" aria-label="Street map of the office location" style="left:63px;top:3216px;width:317px;height:184px;background:linear-gradient(135deg,#e6ecd9,#d6e3c6 50%,#ebe7dc)"></div>
    <div class="info">
      <div class="row" style="top:36px">
        <svg width="9" height="9" viewBox="0 0 10 10"><path d="M2 1 L4 1 L5 3.5 L3.7 4.5 Q5 6.5 6.5 7.3 L7.5 6 L9.5 7 L9.5 9 Q4 9.5 1 2 Z" fill="none" stroke="#3d4a5c" stroke-width=".8"/></svg>(+44) 7900 481 236</div>
      <div class="row" style="top:58px">
        <svg width="9" height="8" viewBox="0 0 10 8"><rect x=".5" y=".5" width="9" height="7" fill="none" stroke="#3d4a5c" stroke-width=".8"/><path d="M.5 .5 L5 4.5 L9.5 .5" fill="none" stroke="#3d4a5c" stroke-width=".8"/></svg>hi@harlow-vectors.example</div>
      <div class="row" style="top:80px">
        <svg width="8" height="10" viewBox="0 0 8 10"><path d="M4 9.5 Q0.5 5.5 .5 3.7 A3.5 3.5 0 0 1 7.5 3.7 Q7.5 5.5 4 9.5Z" fill="none" stroke="#3d4a5c" stroke-width=".8"/><circle cx="4" cy="3.7" r="1.2" fill="none" stroke="#3d4a5c" stroke-width=".8"/></svg>14 Orchard Lane Harlow HW2 4QT</div>
      <div class="btn" style="left:46px;top:101px;width:101px;height:24px">Contact Now</div>
    </div>
  </section>

  <footer class="foot">
    <div class="mark">Harlow Vectors</div>
    <nav><span>HOME</span><span>ABOUT</span><span>APPROACH</span><span>VALUE</span><span>CULTURE</span></nav>
    <div class="social"><span></span><span></span><span></span><span></span><span></span></div>
    <div class="divider"></div>
    <div class="legal">© 2021 Harlow Vectors - All Rights Reserved</div>
  </footer>

</div>
</body>
</html>
```